Verpackungsdesign für CBD-Öl
Herr Felnhorst hat unsere Erwartungen übertroffen. Er gab uns Hilfestellungen und Service in jeglicher Hinsicht. Wir würden Ihn wieder buchen. Er ist absolut empfehlenswert. Vielen Dank
Zielgruppe
Wir möchten im Web-shop Hanföl verkaufen und Leute von 25 -65 Jahren ansprechen
Aufgabenstellung
1. Erstellung eines Designs für eine Verpackung von CBD-Öl. Die Verpackung sollte modern und clean designt werden.
Für Frauen und Männer gleichermaßen
Größe der Faltschachtel: Länge 28 mm, Breite 28 mm, Höhe 94 mm
Ähnlich gewünschtes Designl: die weiße Verpackung von 'Pure Vantis' wäre das Muster. Weiße Schachtel, schwarze Schrift und ein grüner Balken, das um die ganze Schachtel geht als Abgrenzung. Unser selbst kreiertes Logo mit dem selben Grün reichen wir nach.
Auf Anfragen können wir auch eine Beispielbild von Pure Vantis nachreichen.
2. Erstellung Design für das Etikett für die 10-ml-Flasche.
Größe Etikett: Länge: 76 mm, Höhe: 32 mm

```html
<!DOCTYPE html>
<html lang="de">
<head>
<meta charset="utf-8">
<title>Lumera Hanfextrakt – Faltschachtel und Etikett</title>
<link rel="stylesheet" href="https://fonts.googleapis.com/css2?family=Questrial&family=Roboto+Condensed:wght@300;400&display=swap">
<style>
  :root {
    --canvas: #f3f4f2;
    --paper: #ffffff;
    --edge: #e1e3e0;
    --ink: #3b3b3b;
    --ink-soft: #555555;
    --sage: #cfe3d2;
    --sage-text: #a8ccb0;
  }
  * { margin: 0; padding: 0; box-sizing: border-box; }
  html, body { width: 1200px; height: 1200px; overflow: hidden; }
  body {
    position: relative;
    background: var(--canvas);
    font-family: "Questrial", sans-serif;
    color: var(--ink);
  }

  /* Faltschachtel: Seite + Front */
  .carton {
    position: absolute;
    left: 90px; top: 197px;
    display: flex;
    height: 806px;
  }
  .carton-panel {
    position: relative;
    width: 240px; height: 806px;
    background: var(--paper);
    border: 1px solid var(--edge);
  }
  .carton-panel + .carton-panel { border-left: 1px dashed var(--edge); }

  .wrap-band {
    position: absolute;
    left: 0; right: 0; top: 530px;
    height: 52px;
    background: var(--sage);
  }

  /* Seitenteil */
  .side-copy {
    position: absolute;
    left: 22px; right: 22px; top: 140px;
    font-family: "Roboto Condensed", sans-serif;
    font-weight: 300;
    font-size: 15px;
    line-height: 1.45;
    color: var(--ink-soft);
    text-align: justify;
  }
  .side-copy .notice,
  .side-copy .label {
    color: var(--sage-text);
    text-transform: uppercase;
    font-weight: 400;
  }
  .side-copy .notice { font-size: 17px; line-height: 1.2; margin-bottom: 26px; }
  .side-copy .label { font-size: 16px; margin-bottom: 6px; }
  .side-copy p + .label { margin-top: 24px; }

  /* Markenzeile: reiner Schriftzug */
  .brand {
    color: var(--ink);
    font-family: "Questrial", sans-serif;
    font-weight: 400;
    line-height: 1;
    white-space: nowrap;
  }
  .carton-front .brand {
    position: absolute;
    left: 22px; top: 372px;
    font-size: 50px;
  }

  .volume {
    position: absolute;
    left: 30px; top: 530px;
    height: 52px;
    line-height: 52px;
    color: var(--paper);
    font-size: 28px;
    letter-spacing: 0.5px;
  }

  .product {
    position: absolute;
    left: 28px; right: 14px; top: 640px;
  }
  .product-name { font-size: 31px; font-weight: 400; margin-bottom: 14px; }
  .product-desc { font-size: 16.5px; line-height: 1.4; color: var(--ink-soft); }

  /* Flaschenetikett 76 × 32 mm */
  .bottle-label {
    position: absolute;
    left: 650px; top: 504px;
    width: 456px; height: 192px;
    background: var(--paper);
    border: 1px solid var(--edge);
  }
  .bottle-label .brand {
    position: absolute;
    left: 0; right: 0; top: 22px;
    text-align: center;
    font-size: 42px;
  }
  .label-rule {
    position: absolute;
    left: 0; right: 0; top: 84px;
    height: 9px;
    background: var(--sage);
  }
  .bottle-label .product { left: 110px; right: 20px; top: 104px; }
  .bottle-label .product-name { font-size: 24px; margin-bottom: 4px; }
  .bottle-label .product-desc { font-size: 12.5px; line-height: 1.35; }
</style>
</head>
<body>

  <section class="carton" aria-label="Faltschachtel 28 × 28 × 94 mm">
    <div class="carton-panel carton-side">
      <div class="wrap-band"></div>
      <div class="side-copy">
        <div class="notice">Dieses Produkt ist<br>kein Arzneimittel!</div>
        <div class="label">Aromaöl:</div>
        <p>Zur topischen Anwendung geeignet.</p>
        <div class="label">Lagerung:</div>
        <p>Trocken, kühl und lichtgeschützt lagern. Vor Anwendung schütteln. Nicht verwenden während der Schwangerschaft und Stillzeit. Außerhalb der Reichweite von Kindern aufbewahren.</p>
      </div>
    </div>

    <div class="carton-panel carton-front">
      <div class="brand">Lumera</div>
      <div class="wrap-band"></div>
      <div class="volume">10 ml&nbsp; e</div>
      <div class="product">
        <h1 class="product-name">Hanfextrakt</h1>
        <p class="product-desc">mit 1000 mg CBD/CBDA,<br>schonend CO2-extrahiert.<br>Sonnenblumenkernöl.</p>
      </div>
    </div>
  </section>

  <section class="bottle-label" aria-label="Flaschenetikett 76 × 32 mm">
    <div class="brand">Lumera</div>
    <div class="label-rule"></div>
    <div class="product">
      <h2 class="product-name">Hanfextrakt</h2>
      <p class="product-desc">mit 1000 mg CBD/CBDA,<br>schonend CO2-extrahiert.<br>Sonnenblumenkernöl.</p>
    </div>
  </section>

</body>
</html>
```